Health & Wellness Website

Corvanta focuses on helping people with chronic health conditions through communication, education and behavior management. See the attached summary for more info on the company.

The attached wire frames should be turned into a very intuitive and simple website design. The design should have a minimal, modern, and yet still personal feel since the main point of the site is for people with chronic health conditions to be able to express themselves and find others that are like them.

There are 18 pages in the wire frames, but most of them have very similar content and page layouts. The design of the pages should to be as similar to each other as possible with most of the features and formats being repeated. The layout is not set in stone and the primary focus should be on intuitive use.

There should be two versions of the designs: one for tablets in the portrait mode (768 px) and one in the landscape mode (1024 px). These layouts should be included in the winning design.

If you would like to submit one page, I will check the posting and give feedback frequently so you don't waste your time and have to change everything.

Target Market(s)

The target market for this website has two different groups within the overall chronic health patient umbrella. The primary group are people who are under 55 yrs old and already use one or more social media sites. The other group consists of people that are older and less familiar with modern websites. The site needs to be catered to the latter and be incredibly intuitive.

Industry/Entity Type

Education

Requirements
Must have
• INTUITIVE DESIGN that is simple, minimal, and modern with a limited color palette. Tablet landscape and portrait versions are needed. Adobe Fireworks is the preferred program and will give submitted designs a huge leg up in the decision. Adobe Photoshop is the only other acceptable program to use. The designer will also need to make the social media icons, buttons, and other graphic design items that are needed for to go along with the theme. These should be vector graphics and be created either in Adobe Fireworks or Illustrator. All working files for the pages, icons, and graphics will be required once the winner is chosen.
• The necessary pages include: the landing page (long scrolling page with about and community sections); a general modal pop-up layout that includes forms and text; the template for inside of the members area (Home Page in wire frames); the community page; and the profile page (with tabs). Please include all the pages you feel it takes to communicate your design.
Nice to have
• Descriptions of transition effects and notes for the programmers are a good thing. The designer might consider adding navigation on the public landing page that scrolls with the header (This is not in the wire frames).
Should not have
• Flashy or complex features that require a lot of code to accomplish. Should not look like Pagelink.

```html
<!DOCTYPE html>
<html lang="en">
<head>
<meta charset="utf-8">
<title>Corvanta — Persist, Share and Prosper</title>
<link rel="stylesheet" href="https://fonts.googleapis.com/css2?family=Raleway:wght@300;400;500;600&display=swap">
<style>
  :root{
    --ink:#1f1f24;
    --text:#3a3a40;
    --muted:#6d6d75;
    --slate:#4a4858;
    --slate-dark:#3d3b49;
    --gold:#e8b10e;
    --line:#dcdce0;
    --link:#3d8fd6;
    --white:#ffffff;
    --field:#ffffff;
  }
  *{box-sizing:border-box;margin:0;padding:0}
  html,body{width:1200px;height:2517px;overflow:hidden;background:var(--white)}
  body{font-family:"Raleway",sans-serif;color:var(--text);position:relative}
  .abs{position:absolute}

  /* header */
  .brand{left:70px;top:18px;width:230px;height:100px}
  .brand-mark{position:absolute;left:66px;top:0;width:72px;height:58px;background:var(--slate-dark)}
  .brand-name{position:absolute;left:0;top:78px;font-size:25px;font-weight:500;letter-spacing:8px;color:var(--slate-dark)}
  .btn-slate{background:#7a7888;color:var(--white);font-size:15px;display:flex;align-items:center;justify-content:center}
  .signup-top{left:565px;top:71px;width:110px;height:36px}
  .field{background:var(--field);border:1px solid #b9b9c0;font-size:13px;color:#555;padding-left:10px;display:flex;align-items:center;height:36px;top:71px}
  .field-email{left:717px;width:146px}
  .field-pass{left:876px;width:144px}
  .login{left:1028px;top:71px;width:111px;height:36px}
  .remember{left:717px;top:111px;font-size:11px;color:#333;display:flex;align-items:center;gap:6px}
  .remember i{width:11px;height:11px;border:1px solid #888;display:inline-block;position:relative}
  .remember i::after{content:"";position:absolute;left:3px;top:0;width:3px;height:7px;border:solid #333;border-width:0 2px 2px 0;transform:rotate(45deg)}

  /* nav */
  .nav{left:70px;top:147px;width:1071px;height:59px;background:var(--slate)}
  .nav a{position:absolute;top:0;height:59px;display:flex;align-items:center;color:var(--white);font-size:17px;text-decoration:none;transform:translateX(-50%)}
  .nav .sep{position:absolute;top:8px;width:1px;height:43px;background:#67657a}
  .nav .social{font-size:14px;font-weight:600}

  /* hero */
  .hero{left:70px;top:208px;width:1071px;height:394px;border:1px solid var(--line);overflow:hidden}
  .hero-photo{position:absolute;inset:0;background:linear-gradient(100deg,#f6f5f3 0%,#efece8 40%,#e6d2c5 62%,#f3ece7 80%,#e9e6e4 100%)}
  .hero-title{left:114px;top:88px;font-size:43px;font-weight:400;color:var(--ink);white-space:nowrap}
  .hero-sub{left:116px;top:140px;font-size:20px;color:var(--text);white-space:nowrap}
  .hero-cta{left:116px;top:186px;width:178px;height:38px;background:var(--gold);color:var(--white);font-size:20px;display:flex;align-items:center;justify-content:center}
  .hero-arrow{top:150px;width:30px;height:60px}
  .dots{left:120px;top:352px;display:flex;gap:10px}
  .dots span{width:11px;height:11px;border-radius:50%;background:#3a3a40}
  .dots span:first-child{background:transparent;border:1px solid #3a3a40}

  /* boxes */
  .panel{border:1px solid var(--line);background:var(--white)}
  .section-title{font-size:44px;font-weight:400;color:var(--ink);text-align:center;letter-spacing:1px}
  .who{left:70px;top:631px;width:1071px;height:223px}
  .who .section-title{position:absolute;top:24px;width:100%}
  .who-sub{position:absolute;top:75px;width:100%;text-align:center;font-size:20px}
  .who-body{position:absolute;top:123px;left:40px;right:40px;text-align:center;font-size:19px;line-height:28px;color:var(--ink)}

  .card{top:883px;width:347px;height:252px;text-align:center}
  .card svg{position:absolute;left:50%;transform:translateX(-50%);top:48px}
  .card h3{position:absolute;top:152px;width:100%;font-size:26px;font-weight:400;color:var(--ink)}
  .card .more{position:absolute;top:193px;left:50%;transform:translateX(-50%);width:142px;height:36px;background:var(--slate-dark);color:var(--white);font-size:15px;display:flex;align-items:center;justify-content:center}

  .whatwe{left:70px;top:1206px;width:1071px;height:365px}
  .whatwe .section-title{position:absolute;top:40px;width:100%}
  .whatwe-lead{position:absolute;top:102px;width:100%;text-align:center;font-size:19px;line-height:27px;color:var(--ink)}
  .whatwe-body{position:absolute;top:172px;left:50px;right:50px;text-align:center;font-size:14.5px;line-height:23px;color:var(--text)}

  /* team */
  .team-title{left:0;top:1640px;width:1200px;font-size:40px}
  .member{top:1718px;width:347px}
  .member .photo{height:214px;border:1px solid var(--line)}
  .member h4{margin-top:22px;font-size:26px;font-weight:400;color:var(--ink)}
  .member p{margin-top:6px;font-size:15px;line-height:21px;color:var(--text)}

  /* posts */
  .posts-title{left:66px;top:2100px;font-size:30px;font-weight:400;color:var(--ink);white-space:nowrap}
  .posts-intro{left:70px;top:2162px;width:540px;font-size:14.5px;line-height:21px;color:var(--text)}
  .posts-intro p{margin-bottom:21px}
  .posts-card{left:637px;top:2113px;width:504px;height:267px}
  .post{position:absolute;left:58px;width:400px}
  .post h5{font-size:21px;font-weight:400;color:var(--ink)}
  .post p{margin-top:8px;font-size:12.5px;line-height:17px;color:var(--text)}
  .post p span{color:var(--link);margin-left:28px}
  .chev{top:118px;width:16px;height:32px}

  /* footer */
  .foot-line{left:70px;top:2413px;width:1071px;height:1px;background:var(--line)}
  .foot-nav{left:70px;top:2448px;display:flex;gap:14px;font-size:16px;color:var(--ink)}
  .foot-legal{left:70px;top:2482px;font-size:12.5px;color:var(--ink)}
  .foot-social{top:2445px;right:59px;display:flex;align-items:center;gap:18px;font-size:14px;font-weight:600;color:var(--ink)}
  .copyright{right:59px;top:2486px;font-size:12px;color:var(--ink)}
</style>
</head>
<body>

<header>
  <div class="abs brand">
    <div class="brand-mark"></div>
    <div class="brand-name">CORVANTA</div>
  </div>
  <div class="abs btn-slate signup-top">Sign Up</div>
  <div class="abs field field-email">Email</div>
  <div class="abs field field-pass">Password</div>
  <div class="abs btn-slate login">Log In</div>
  <div class="abs remember"><i></i>Remember me</div>
</header>

<nav class="abs nav">
  <a style="left:135px">HOME</a>
  <span class="sep" style="left:211px"></span>
  <a style="left:317px">COMMUNITY</a>
  <span class="sep" style="left:421px"></span>
  <a style="left:518px">PORTFOLIO</a>
  <a style="left:776px" aria-label="Email">
    <svg width="30" height="20" viewBox="0 0 30 20"><rect x="1" y="1" width="28" height="18" fill="#fff"/><path d="M1 1 L15 12 L29 1" fill="none" stroke="#4a4858" stroke-width="2"/></svg>
  </a>
  <span class="sep" style="left:844px"></span>
  <a class="social" style="left:898px">Pagelink</a>
  <a class="social" style="left:965px">Chirply</a>
  <a class="social" style="left:1027px">Circlo</a>
</nav>

<section class="abs hero">
  <div class="hero-photo" role="img" aria-label="Photo of a person meditating, hand resting in a calm pose in soft daylight"></div>
  <h1 class="abs hero-title">Persist, Share and Prosper</h1>
  <div class="abs hero-sub">Lorem ipsum dolor sit amet, consectetur adipiscing elit</div>
  <div class="abs hero-cta">Learn More</div>
  <svg class="abs hero-arrow" style="left:36px" viewBox="0 0 30 60"><path d="M27 2 L3 30 L27 58" fill="none" stroke="#1f1f24" stroke-width="3"/></svg>
  <svg class="abs hero-arrow" style="left:1000px" viewBox="0 0 30 60"><path d="M3 2 L27 30 L3 58" fill="none" stroke="#1f1f24" stroke-width="3"/></svg>
  <div class="abs dots"><span></span><span></span><span></span><span></span></div>
</section>

<section class="abs panel who">
  <h2 class="section-title">WHO WE ARE</h2>
  <div class="who-sub">Persist, Share and Prosper</div>
  <p class="who-body">Corvanta is an online, community centric approach to wellness through education, communication, and behavioral management for people with chronic health conditions.</p>
</section>

<section>
  <div class="abs panel card" style="left:70px">
    <svg width="60" height="74" viewBox="0 0 60 74"><path d="M30 2 C14 2 3 14 3 29 C3 47 30 72 30 72 C30 72 57 47 57 29 C57 14 46 2 30 2 Z" fill="#3d3b49"/><circle cx="30" cy="28" r="9" fill="#fff"/></svg>
    <h3>About Corvanta</h3>
    <div class="more">READ MORE</div>
  </div>
  <div class="abs panel card" style="left:432px">
    <svg width="58" height="70" viewBox="0 0 58 70"><circle cx="29" cy="20" r="15" fill="#3d3b49"/><path d="M2 68 C2 50 14 40 29 40 C44 40 56 50 56 68 Z" fill="#3d3b49"/></svg>
    <h3>Community Highlights</h3>
    <div class="more">READ MORE</div>
  </div>
  <div class="abs panel card" style="left:791px">
    <svg width="70" height="70" viewBox="0 0 70 70"><path d="M44 10 H10 A5 5 0 0 0 5 15 V60 A5 5 0 0 0 10 65 H55 A5 5 0 0 0 60 60 V28" fill="none" stroke="#3d3b49" stroke-width="5"/><path d="M56 4 L66 14 L36 44 L24 47 L27 35 Z" fill="#3d3b49"/></svg>
    <h3>Sign Up</h3>
    <div class="more">READ MORE</div>
  </div>
</section>

<section class="abs panel whatwe">
  <h2 class="section-title">WHAT WE DO</h2>
  <p class="whatwe-lead">Members of Corvanta's community know how life changes when we have chronic medical conditions.<br>Our members know how grim things can be. And our community also knows how bright things can become.</p>
  <p class="whatwe-body">Although Corvanta does not replace your other medical services, it will compliment them. People who use Corvanta become more motivated and hopeful. They learn about all the research-based strategies they can use to maintain the gains they've made with their chronic disease, while also preventing stress, or mood difficulties, which also arise from time when people live with chronic medical conditions. As members of this online community offer help and seek help from one another, they are also exposed to health information which educates and motivates users to live the most satisfying lives they can live with their chronic health condition. Corvanta's wellness platform helps users connect with other users like you to share support, information, and ideas. By checking in with you about how you are doing and what you are doing about your health, we improve.</p>
</section>

<h2 class="abs section-title team-title">CORVANTA TEAM</h2>
<div class="abs member" style="left:70px">
  <div class="photo" role="img" aria-label="Portrait photo of a team member in a white medical coat" style="background:linear-gradient(180deg,#f2f2f2,#e7e4e2)"></div>
  <h4>Dana Whitlow</h4>
  <p>Lorem ipsum dolor sit amet, consectetur adipiscing elit. Sed at ante. Mauris eleifend, quam a vulputate dictum, massa.</p>
</div>
<div class="abs member" style="left:432px">
  <div class="photo" role="img" aria-label="Photo of a team member resting on a sunny lawn" style="background:linear-gradient(180deg,#c9c18a,#8d9a4e 60%,#6f7d3a)"></div>
  <h4>Rae Colton</h4>
  <p>Lorem ipsum dolor sit amet, consectetur adipiscing elit. Sed at ante. Mauris eleifend, quam a vulputate dictum, massa.</p>
</div>
<div class="abs member" style="left:791px">
  <div class="photo" role="img" aria-label="Portrait photo of two team members in a bright office" style="background:linear-gradient(100deg,#e9ecee,#d9d2c4 55%,#c9c6c2)"></div>
  <h4>Mira Ellison</h4>
  <p>Lorem ipsum dolor sit amet, consectetur adipiscing elit. Sed at ante. Mauris eleifend, quam a vulputate dictum, massa.</p>
</div>

<h2 class="abs posts-title">Selected Posts From Corvanta Members</h2>
<div class="abs posts-intro">
  <p>These posts were written by members inside of the Corvanta community. They are honest representations of the kinds of interactions going on and we are excited that the authors have allowed you to view them outside of the safe community environment.</p>
  <p>Feel free to read through them and see what you think. These are just a handful of the many posts from members that have the same struggles and triumphs over their health conditions that you might be here for.</p>
  <p>Enjoy!</p>
</div>
<div class="abs panel posts-card">
  <svg class="abs chev" style="left:14px" viewBox="0 0 16 32"><path d="M14 2 L2 16 L14 30" fill="none" stroke="#bbb" stroke-width="2"/></svg>
  <svg class="abs chev" style="left:474px" viewBox="0 0 16 32"><path d="M2 2 L14 16 L2 30" fill="none" stroke="#555" stroke-width="2"/></svg>
  <div class="post" style="top:32px">
    <h5>Owen Pratt</h5>
    <p>Lorem ipsum dolor sit amet, consectetur adipiscing elit. Sed at ante. Mauris eleifend, quam a vulputate dictum, massa quam dapibus leo, eget vulputate... <span>&gt; Read More</span></p>
  </div>
  <div class="post" style="top:150px">
    <h5>Lena Marsh</h5>
    <p>Lorem ipsum dolor sit amet, consectetur adipiscing elit. Sed at ante. Mauris eleifend, quam a vulputate dictum, massa quam dapibus leo, eget vulputate... <span>&gt; Read More</span></p>
  </div>
</div>

<footer>
  <div class="abs foot-line"></div>
  <div class="abs foot-nav"><span>HOME</span><span>ABOUT US</span><span>HEALTHCARE</span><span>SERVICES</span><span>CONTACT US</span><span>CHRONIC CONDITIONS</span></div>
  <div class="abs foot-legal">Terms of Use &amp; Privacy Policy</div>
  <div class="abs foot-social">
    <svg width="32" height="22" viewBox="0 0 32 22" aria-label="Email"><rect x="1" y="1" width="30" height="20" fill="#1f1f24"/><path d="M1 1 L16 13 L31 1" fill="none" stroke="#fff" stroke-width="2"/></svg>
    <span>Pagelink</span><span>Chirply</span><span>Circlo</span>
  </div>
  <div class="abs copyright">© Copyright 2013. All Rights Reserved.</div>
</footer>

</body>
</html>
```